Professional and creative business card design for recruiting service providers

Our company supports German medium-sized companies in filling vacancies promptly. For this we use social media marketing and bring our customers into the visibility.

We want a professional but also creative design for our business cards.

Please look at valdringer-kollegen.de to get an impression of our CI.

Target Market(s)

Small and medium-sized companies in Germany from the industry

Industry/Entity Type

Industrie, Handwerk

Contact Information for Business Card

Name, Position, Telefonnummer, Email, Website

Colors
EE7325
F08F49
F5BC92
FAE3D3
FDF4ED

Requirements
Must have
• A picture of the employee and in the style of www.valdringer-kollegen.de

```html
<!DOCTYPE html>
<html lang="de">
<head>
<meta charset="utf-8">
<title>Valdringer &amp; Kollegen – Visitenkarte</title>
<link href="https://fonts.googleapis.com/css2?family=Montserrat:wght@700&family=Arimo:wght@400;700&display=swap" rel="stylesheet">
<style>
  :root {
    --orange: #ee7325;
    --orange-soft: #f08f49;
    --ink: #2a2a2a;
    --text: #333333;
    --paper: #ffffff;
    --card-dark: #2c2c2c;
    --backdrop: #e8e8e8;
    --photo-top: #c9c6c4;
    --photo-bottom: #1e1f24;
  }
  * { box-sizing: border-box; margin: 0; padding: 0; }
  html, body { width: 1200px; height: 802px; overflow: hidden; }
  body {
    background: var(--backdrop);
    font-family: "Arimo", Arial, sans-serif;
    position: relative;
  }
  .card {
    position: absolute;
    top: 226px;
    width: 540px;
    height: 350px;
    border-radius: 4px;
    box-shadow: 0 8px 24px rgba(0,0,0,0.18);
    overflow: hidden;
  }
  /* Front */
  .card-front { left: 40px; background: var(--paper); }
  .front-brand {
    position: absolute; left: 34px; top: 40px;
    display: flex; align-items: center; gap: 14px;
  }
  .brand-square { width: 34px; height: 34px; background: var(--orange); }
  .brand-name {
    font-family: "Montserrat", sans-serif; font-weight: 700;
    font-size: 21px; line-height: 1.1; letter-spacing: 1.5px;
    color: var(--ink); text-transform: uppercase;
  }
  .person { position: absolute; left: 34px; top: 128px; }
  .person-name {
    font-size: 20px; font-weight: 400; letter-spacing: 0.5px;
    color: var(--orange); text-transform: uppercase;
  }
  .person-role { font-size: 15px; color: var(--text); margin-top: 3px; }
  .address { position: absolute; left: 34px; top: 196px; font-size: 14px; line-height: 1.3; color: var(--text); }
  .contact { position: absolute; left: 34px; top: 250px; list-style: none; font-size: 14px; color: var(--text); }
  .contact li { display: flex; align-items: center; gap: 9px; line-height: 1.4; }
  .contact svg { width: 12px; height: 12px; flex: none; }
  .employee-photo {
    position: absolute; right: 0; top: 0; width: 230px; height: 350px;
    background: linear-gradient(180deg, var(--photo-top) 0%, #5a5655 38%, var(--photo-bottom) 70%);
  }
  /* Back */
  .card-back { left: 620px; background: var(--card-dark); }
  .back-brand {
    position: absolute; left: 0; right: 0; top: 0; bottom: 0;
    display: flex; align-items: center; justify-content: center; gap: 20px;
  }
  .back-brand .brand-square { width: 46px; height: 46px; }
  .back-brand .brand-name { color: #ffffff; font-size: 30px; letter-spacing: 2.5px; }
</style>
</head>
<body>
  <section class="card card-front" aria-label="Visitenkarte Vorderseite">
    <div class="front-brand">
      <span class="brand-square"></span>
      <span class="brand-name">Valdringer<br>&amp; Kollegen</span>
    </div>
    <div class="person">
      <p class="person-name">Lukas Brenner</p>
      <p class="person-role">Manager</p>
    </div>
    <p class="address">Kastanienweg 17a<br>70190 Stuttgart</p>
    <ul class="contact">
      <li><svg viewBox="0 0 12 12"><path d="M2.5 1h2l1 3-1.3 1a6 6 0 0 0 2.8 2.8L8 6.5l3 1v2A1.5 1.5 0 0 1 9.5 11 8.5 8.5 0 0 1 1 2.5 1.5 1.5 0 0 1 2.5 1z" fill="var(--orange)"/></svg>0171 394 2207</li>
      <li><svg viewBox="0 0 12 12"><rect x="1" y="2.5" width="10" height="7" fill="none" stroke="var(--orange)" stroke-width="1.2"/><path d="M1 2.5l5 4 5-4" fill="none" stroke="var(--orange)" stroke-width="1.2"/></svg>info@valdringer-kollegen.de</li>
      <li><svg viewBox="0 0 12 12"><circle cx="6" cy="6" r="5" fill="none" stroke="var(--orange)" stroke-width="1.2"/><ellipse cx="6" cy="6" rx="2.2" ry="5" fill="none" stroke="var(--orange)" stroke-width="1"/><path d="M1 6h10" stroke="var(--orange)" stroke-width="1"/></svg>www.valdringer-kollegen.de</li>
    </ul>
    <div class="employee-photo" role="img" aria-label="Porträtfoto des Mitarbeiters im dunklen Sakko"></div>
  </section>

  <section class="card card-back" aria-label="Visitenkarte Rückseite">
    <div class="back-brand">
      <span class="brand-square"></span>
      <span class="brand-name">Valdringer<br>&amp; Kollegen</span>
    </div>
  </section>
</body>
</html>
```